Box packaging design for Bivvo Cheese Knives Set

We would like a box design that is elegant and sophisticated. A box that would be great for gift giving. We are open to your creative ideas. Simple yet chic.

We also want a diagram of the 6 knives on the inside of the top of the lid to show what each knife is used for...you can see an example of it at the below link. We do not want to copy them...this is only for reference.

We will have text on the bottom of the box and "Made in China" somewhere on the box along with the UPC code. The 6 piece knife set is just like the Torvel set in the below link.

https://www.shopvarnel.example/TORVEL-Premium-6-Piece-Cheese-Knife/item/K73QP2XW8R/ref=sr_1_5?s=home-garden&ie=UTF8&qid=1402637719&sr=1-5&keywords=cheese+knives

Bivvo, the name of our company means, "celebrate life."
Our company is all about the Home.
We specialize in very upscale, high-end products for dining, entertaining and cooking.

Attached is the logo that will go on the top of the box. (RGB bivvo.eps)
WE WILL NOT BE USING THE TEXT - (Tools for Discerning Hosts) ONLY the Word Bivvo and the Z.

Attached is a picture of the set of cheese knives that will be going into
the box you will be designing. (Pic of cheese knives.jpg)

Also, attached is a product that we will be selling along with the cheese
knives which will be a second box to design to go along with the first one.
(Cheese marker 5 piece set).

The cheese knife insert card will also need to be designed to go inside the
box. (Cheese knife insert card.png)

On the back of the box we will provide you with a UPC code and where the
UPC code is...please type Made in China as show in the attachment. (UPS
code with Made in China)

Also, on the back of the box ..please add the attached text.

Good luck and best wishes!

1. The Bivvo logo goes on the top of the box.
2. On the inside top of the box we want a diagram of the cheese knives similar to the below link but we can't copy it...if you also look at the card insert attached in the original project instructions you can see the diagram there.

Inside the top of the box will show each knife and what each knife does, for example. Do a silhouette of the knives and under each one will have text with what they are used for.... such as: Hard - Soft - Spread - Serving Fork - etc.

https://lnkpoint.example/images/7Tq4Rm

3. Bottom of box is the same as top size...see attached template for cheese knives box template.... Some text will be on the bottom which i will upload shortly and a UPC code in lower right hand corner with Made in China on it...see attached UPC code for reference.

I attached the cheese marker box template and the insert card template.

Let me know if you have any other questions....and best wishes...Marla

Target Market(s)

Our target audience are people who love to cook, entertain and celebrate life, high-end consumer catering to the luxury market.

Industry/Entity Type

Cooking

Colors
9bcb3b
abd036

Requirements
Must have
• simple yet sophisticated and chic
Nice to have
• We are open to your ideas ...
Should not have
• You can see the attached templates....PLEASE NOTE....the cheese marker template is NOT our design on it...they only sent this over to use the actual template.

```html
<!DOCTYPE html>
<html lang="en">
<head>
<meta charset="utf-8">
<title>Bivvo Cheese Knives Box – Lid Dieline</title>
<link rel="stylesheet" href="https://fonts.googleapis.com/css2?family=Montserrat:wght@300;500;700&display=swap">
<style>
  :root {
    --mint: #69ffcc;
    --lid-black: #0e0f0f;
    --band-black: #070909;
    --paper: #ffffff;
    --fold-shadow: #9a9a9a;
    --label-grey: #8c8c8c;
  }
  html, body {
    margin: 0;
    padding: 0;
    width: 1200px;
    height: 1052px;
    overflow: hidden;
    background: var(--paper);
  }
  .dieline {
    display: block;
    width: 1200px;
    height: 1052px;
  }
  .flap, .side-panel { fill: var(--mint); }
  .flap-shadow { fill: var(--fold-shadow); }
  .lid-face { fill: var(--lid-black); }
  .centre-band { fill: var(--band-black); }
  .brand-mark { fill: var(--mint); }
  .brand-tag { fill: var(--band-black); }
  .brand-name {
    font-family: "Montserrat", sans-serif;
    font-weight: 500;
    fill: var(--mint);
  }
  .lid-title {
    font-family: "Montserrat", sans-serif;
    font-weight: 700;
    font-size: 12.5px;
    fill: #ffffff;
    letter-spacing: 0.2px;
  }
  .side-title {
    font-family: "Montserrat", sans-serif;
    font-weight: 700;
    font-size: 11.5px;
  }
  .side-title.dark { fill: var(--band-black); }
  .side-title.light { fill: #ffffff; font-weight: 500; }
  .panel-label {
    font-family: "Montserrat", sans-serif;
    font-weight: 300;
    font-size: 34px;
    fill: var(--label-grey);
  }
</style>
</head>
<body>
<svg class="dieline" viewBox="0 0 1200 1052" xmlns="http://www.w3.org/2000/svg">
  <!-- fold shadows -->
  <g class="shadows">
    <rect class="flap-shadow" x="128" y="69" width="950" height="108"/>
    <rect class="flap-shadow" x="128" y="780" width="950" height="108"/>
    <rect class="flap-shadow" x="20" y="177" width="108" height="603"/>
    <rect class="flap-shadow" x="1078" y="177" width="108" height="603"/>
  </g>

  <!-- top flap with corner tabs -->
  <rect class="flap" x="126" y="67" width="950" height="108"/>
  <polygon class="flap" points="126,122 72,130 72,166 126,175"/>
  <polygon class="flap" points="1076,122 1130,130 1130,166 1076,175"/>

  <!-- bottom flap with corner tabs -->
  <rect class="flap" x="126" y="778" width="950" height="108"/>
  <polygon class="flap" points="126,786 72,794 72,824 126,832"/>
  <polygon class="flap" points="1076,786 1130,794 1130,824 1076,832"/>

  <!-- side panels -->
  <rect class="side-panel" x="18" y="175" width="108" height="603"/>
  <rect class="side-panel" x="1076" y="175" width="108" height="603"/>

  <!-- lid face -->
  <rect class="lid-face" x="126" y="175" width="950" height="603"/>
  <rect class="centre-band" x="454" y="175" width="293" height="415"/>
  <rect class="centre-band" x="454" y="725" width="293" height="53"/>

  <!-- central brand lockup -->
  <rect class="brand-mark" x="555" y="398" width="91" height="91"/>
  <text class="brand-name" x="600" y="538" font-size="36" letter-spacing="17" text-anchor="middle">BIVVO</text>

  <text class="lid-title" x="600" y="715" text-anchor="middle">PREMIUM 6-PIECES CHEESE KNIVES SET</text>

  <!-- left side panel -->
  <rect class="brand-tag" x="71" y="230" width="55" height="70"/>
  <rect class="brand-mark" x="93" y="254" width="21" height="21"/>
  <text class="brand-name" font-size="8" letter-spacing="4" text-anchor="middle" transform="translate(83 265) rotate(90)">BIVVO</text>
  <text class="side-title dark" text-anchor="middle" transform="translate(102 476) rotate(90)">PREMIUM 6 PIECE CHEESE KNIFE SET</text>
  <text class="side-title light" text-anchor="middle" transform="translate(86 476) rotate(90)">WITH CHEESE MARKER 5 PIECE SET</text>

  <!-- right side panel -->
  <rect class="brand-tag" x="1076" y="654" width="54" height="70"/>
  <rect class="brand-mark" x="1085" y="678" width="21" height="21"/>
  <text class="brand-name" font-size="8" letter-spacing="4" text-anchor="middle" transform="translate(1117 689) rotate(-90)">BIVVO</text>
  <text class="side-title dark" text-anchor="middle" transform="translate(1099 476) rotate(-90)">PREMIUM 6 PIECE CHEESE KNIFE SET</text>
  <text class="side-title light" text-anchor="middle" transform="translate(1115 476) rotate(-90)">WITH CHEESE MARKER 5 PIECE SET</text>

  <!-- panel label -->
  <text class="panel-label" x="546" y="938" text-anchor="middle">Top</text>
</svg>
</body>
</html>
```